New local Orchid nursery branding

We need a business card designed for our small local company in Darwin, Australia that grows orchids, called Blooms at Carrow.
We will be running private sales from our property, and handing these out at local events for perspective customers.

We would like to see designs that are simple, and able to be used with minimal colours and containing an orchid, preferably a stylised representation instead of a photo.
The eventual hope is to take this into larger formats to create our company logo/branding etc, but for now we just need business cards.

Target Market(s)

Local Orchid

Industry/Entity Type

Business

Contact Information for Business Card

Company Name
Logo
Name
Phone Number
Street Address
Email Address (less prominent than rest of the text)

Font styles to use
Sans Serif

Requirements
Must have
• Name of the company, which is Blooms at Carrow
Nice to have
• stylised orchid logo
Should not have
• too many colours

```html
<!DOCTYPE html>
<html lang="en">
<head>
<meta charset="utf-8">
<title>Blooms at Carrow – Business Card</title>
<link href="https://fonts.googleapis.com/css2?family=Lato:wght@300;400;700&display=swap" rel="stylesheet">
<style>
  :root {
    --page-bg: #e9e6e1;
    --charcoal: #2f2f31;
    --slate: #48484a;
    --divider: #3a3a3c;
    --leaf-green: #5a8a3a;
    --paper: #ffffff;
    --ink-light: #f2f2f2;
    --orchid-pink: #c94a88;
    --orchid-peach: #f2b27a;
  }
  * { margin: 0; padding: 0; box-sizing: border-box; }
  html, body {
    width: 1200px; height: 1047px; overflow: hidden;
    background: var(--page-bg);
    font-family: "Lato", sans-serif;
  }
  .business-card {
    position: absolute; left: 100px; top: 237px;
    width: 1000px; height: 572px;
    background: var(--paper);
    box-shadow: 0 12px 30px rgba(0,0,0,0.18);
    overflow: hidden;
  }
  .contact-panel {
    position: absolute; left: 0; top: 0; width: 470px; height: 100%;
  }
  .identity {
    height: 165px; background: var(--charcoal);
    padding: 82px 0 0 58px;
  }
  .person-name {
    font-size: 38px; line-height: 1; color: var(--leaf-green);
    letter-spacing: 0.5px;
  }
  .person-name strong { font-weight: 700; }
  .person-name span { font-weight: 300; }
  .designation {
    margin-top: 4px; font-size: 20px; font-weight: 400;
    color: var(--ink-light); letter-spacing: 0.6px;
  }
  .contact-row {
    height: 135.67px; background: var(--slate);
    border-top: 2px solid var(--divider);
    display: flex; align-items: center;
    padding-left: 60px; padding-right: 40px;
    color: var(--ink-light);
  }
  .contact-row svg { width: 40px; height: 40px; flex: none; fill: var(--ink-light); }
  .contact-row p {
    margin-left: 58px; font-size: 22px; line-height: 28px; letter-spacing: 0.6px;
    white-space: nowrap;
  }
  .panel-accent {
    position: absolute; left: 450px; top: 165px; width: 20px; height: 407px;
    background: var(--leaf-green);
  }
  .brand-panel {
    position: absolute; left: 470px; top: 0; width: 420px; height: 100%;
    text-align: center;
  }
  .orchid-spray {
    position: absolute; left: 60px; top: 170px; width: 300px; height: 110px;
    border-radius: 55px 55px 30px 30px;
    background: radial-gradient(ellipse at 50% 45%, var(--orchid-pink) 0%, #d98cb0 40%, var(--orchid-peach) 75%, rgba(242,178,122,0) 100%);
  }
  .business-name {
    position: absolute; left: 0; right: 0; top: 304px;
    font-size: 34px; font-weight: 400; color: var(--leaf-green);
    letter-spacing: 0.5px; white-space: nowrap;
  }
  .edge-accent {
    position: absolute; left: 890px; top: 165px; width: 15px; height: 407px;
    background: var(--leaf-green);
  }
  .edge-band {
    position: absolute; left: 905px; top: 0; width: 95px; height: 100%;
    background: linear-gradient(var(--charcoal) 0 165px, var(--slate) 165px 100%);
  }
</style>
</head>
<body>
  <main class="business-card">
    <section class="contact-panel">
      <header class="identity">
        <h1 class="person-name"><strong>YOUR</strong> <span>NAME</span></h1>
        <h2 class="designation">DESIGNATION</h2>
      </header>
      <div class="contact-row">
        <svg viewBox="0 0 40 40" aria-hidden="true"><path d="M20 6 2 21h5v13h10v-9h6v9h10V21h5z"/></svg>
        <p>12 Carrow Orchard Lane<br>Darwin NT 0800</p>
      </div>
      <div class="contact-row">
        <svg viewBox="0 0 40 40" aria-hidden="true" fill="none"><g fill="none" stroke="#f2f2f2" stroke-width="2.5"><circle cx="20" cy="20" r="16"/><ellipse cx="20" cy="20" rx="7" ry="16"/><path d="M4 20h32M7 12h26M7 28h26M20 4v32"/></g></svg>
        <p>hello@bloomsatcarrow.au<br>www.bloomsatcarrow.au</p>
      </div>
      <div class="contact-row">
        <svg viewBox="0 0 40 40" aria-hidden="true"><path d="M3 14c0-5 8-8 17-8s17 3 17 8v3h-8v-4c-3-1-6-1-9-1s-6 0-9 1v4H3z"/><path d="M9 20h22l4 14H5zM15 23h2v2h-2zm4 0h2v2h-2zm4 0h2v2h-2zm-8 4h2v2h-2zm4 0h2v2h-2zm4 0h2v2h-2z"/></svg>
        <p>0400 . 118 . 274<br>08 . 8900 . 3315</p>
      </div>
      <div class="panel-accent"></div>
    </section>
    <section class="brand-panel">
      <div class="orchid-spray" role="img" aria-label="Stylised orchid spray with pink and purple blooms, peach buds and green leaves"></div>
      <p class="business-name">BLOOMS AT CARROW</p>
    </section>
    <div class="edge-accent"></div>
    <div class="edge-band"></div>
  </main>
</body>
</html>
```